Baby Boutique Needs a Business Card Design

We need a modern double sided business card design using the attached logo for T' Tot Nook.

T' Tot Nook is a baby boutique which sells only handmade clothing and accessories for both boys and girls. Our store will live exclusively online.

We would like to only use the colors that have been used in the logo.

Target Market(s)

Potential wholesale clients, Small business owners

Industry/Entity Type

Retail

Contact Information for Business Card

Name Benedict R. Halvorsen (Owner)
Email sales@ttotnook.example
Main Phone 555-203-7164
Cell phone 555-203-7590
Website www.TTotNook.example

Font styles to use
Sans Serif

Colors

Designer to choose colors to be used in the design.

Requirements
Must have
• -Would like to have icons that indentify the contact information.
• -Include our website
• -Include our tagline in a small area near the bottom. "Handmade Baby Creations"
• -Would like to include Facebook and Instagram Icons
• -
Nice to have
• Would like to have a simple back side with the logo.
• Something along the lines of the meridale funding card attached.

```html
<!DOCTYPE html>
<html lang="en">
<head>
<meta charset="utf-8">
<title>T' Tot Nook – Business Card</title>
<link rel="stylesheet" href="https://fonts.googleapis.com/css2?family=Open+Sans:ital,wght@1,700;1,800&family=Quicksand:wght@400;500;600&display=swap">
<style>
  :root {
    --sheet: #e6e6e4;
    --card: #121212;
    --coral: #dd5b5b;
    --teal: #7ccbbb;
    --ink: #141414;
    --paper: #f2f2f2;
    --muted: #9a9a9a;
  }
  * { box-sizing: border-box; margin: 0; padding: 0; }
  html, body { width: 797px; height: 1200px; overflow: hidden; background: var(--sheet); }
  .sheet { position: relative; width: 797px; height: 1200px; background: var(--sheet); font-family: "Quicksand", sans-serif; }

  .side-label {
    position: absolute; left: 0; width: 100%; text-align: center;
    font-family: "Open Sans", sans-serif; font-style: italic; font-weight: 800;
    font-size: 22px; letter-spacing: 4px; color: var(--ink);
  }
  .side-label--front { top: 69px; left: -40px; }
  .side-label--back { top: 529px; left: -50px; }

  .card {
    position: absolute; left: 61px; width: 642px; height: 363px;
    background: var(--card); border-radius: 14px; overflow: hidden;
  }
  .card--front { top: 129px; }
  .card--back { top: 588px; }

  .holder { position: absolute; left: 39px; top: 24px; }
  .holder__name { font-size: 25px; font-weight: 400; color: var(--coral); line-height: 1; white-space: nowrap; }
  .holder__role { position: absolute; left: 4px; top: 34px; font-size: 14px; font-weight: 500; color: var(--muted); letter-spacing: 0.5px; }
  .holder__rule { position: absolute; left: 58px; top: 45px; width: 169px; height: 1px; background: var(--coral); }

  .contact { position: absolute; left: 37px; top: 144px; list-style: none; }
  .contact__item { display: flex; align-items: center; height: 32px; font-size: 16px; color: var(--paper); font-weight: 500; }
  .contact__icon { width: 21px; height: 21px; margin-right: 9px; flex: none; }

  .social { position: absolute; left: 38px; top: 278px; display: flex; gap: 4px; }
  .social__icon { width: 22px; height: 22px; }

  .brand {
    position: absolute; color: var(--teal); font-family: "Quicksand", sans-serif; font-weight: 600;
    text-align: center; white-space: nowrap;
  }
  .card--front .brand { left: 370px; top: 118px; width: 200px; font-size: 42px; line-height: 46px; }
  .card--back .brand { left: 0; width: 100%; top: 112px; font-size: 62px; line-height: 66px; }

  .tagline-band {
    position: absolute; left: 0; bottom: 0; width: 100%; height: 49px; background: var(--coral);
    display: flex; align-items: center; justify-content: center;
    font-size: 20px; letter-spacing: 3.5px; color: var(--paper); font-weight: 400;
  }

  .deliverables {
    position: absolute; left: 146px; top: 1010px; list-style: none;
    font-family: "Open Sans", sans-serif; font-style: italic; font-weight: 800;
    font-size: 22px; letter-spacing: 4px; color: var(--ink); line-height: 30px;
  }
</style>
</head>
<body>
<main class="sheet">
  <h2 class="side-label side-label--front">FRONT SIDE</h2>
  <section class="card card--front">
    <div class="holder">
      <p class="holder__name">Benedict R. Halvorsen</p>
      <p class="holder__role">owner</p>
      <span class="holder__rule"></span>
    </div>

    <ul class="contact">
      <li class="contact__item">
        <svg class="contact__icon" viewBox="0 0 24 24" fill="none" stroke="var(--coral)" stroke-width="1.4"><circle cx="12" cy="12" r="10.5"/><path d="M8 7.5l2 -.5 1.2 2.6-1.3 1c.6 1.3 1.6 2.3 2.9 2.9l1-1.3 2.6 1.2-.5 2c-4.2.2-8.1-3.7-7.9-7.9z" fill="var(--coral)" stroke="none"/></svg>
        555-203-7164
      </li>
      <li class="contact__item">
        <svg class="contact__icon" viewBox="0 0 24 24" fill="none" stroke="var(--coral)" stroke-width="1.4"><circle cx="12" cy="12" r="10.5"/><rect x="9" y="6.5" width="6" height="11" rx="1"/></svg>
        555-203-7590
      </li>
      <li class="contact__item">
        <svg class="contact__icon" viewBox="0 0 24 24" fill="none" stroke="var(--coral)" stroke-width="1.4"><circle cx="12" cy="12" r="10.5"/><rect x="7" y="8.5" width="10" height="7" rx="1" fill="var(--coral)" stroke="none"/><path d="M7.5 9l4.5 3.5 4.5-3.5" stroke="var(--card)" stroke-width="1"/></svg>
        sales@ttotnook.example
      </li>
      <li class="contact__item">
        <svg class="contact__icon" viewBox="0 0 24 24" fill="none" stroke="var(--coral)" stroke-width="1.4"><circle cx="12" cy="12" r="10.5"/><circle cx="12" cy="12" r="5.5"/><path d="M6.5 12h11M12 6.5c-2.5 3-2.5 8 0 11M12 6.5c2.5 3 2.5 8 0 11" stroke-width="1"/></svg>
        www.TTotNook.example
      </li>
    </ul>

    <div class="social" aria-label="Social profiles">
      <svg class="social__icon" viewBox="0 0 24 24" fill="none" stroke="var(--teal)" stroke-width="1.4" aria-label="Share"><circle cx="12" cy="12" r="10.5"/><circle cx="8.5" cy="12" r="1.6" fill="var(--teal)" stroke="none"/><circle cx="15.5" cy="8" r="1.6" fill="var(--teal)" stroke="none"/><circle cx="15.5" cy="16" r="1.6" fill="var(--teal)" stroke="none"/><path d="M8.5 12l7-4M8.5 12l7 4" stroke-width="1.1"/></svg>
      <svg class="social__icon" viewBox="0 0 24 24" fill="none" stroke="var(--teal)" stroke-width="1.4" aria-label="Message"><circle cx="12" cy="12" r="10.5"/><path d="M7 8h10v6.5h-6l-2.5 2v-2H7z" stroke-width="1.2" stroke-linejoin="round"/></svg>
    </div>

    <p class="brand">T' Tot<br>Nook</p>

    <p class="tagline-band">Handmade Baby Creations</p>
  </section>

  <h2 class="side-label side-label--back">BACK SIDE</h2>
  <section class="card card--back">
    <p class="brand">T' Tot<br>Nook</p>
  </section>

  <ol class="deliverables">
    <li>1. EDITABLE AI, EPS, PDF F ILES</li>
    <li>2. FONTS ARE GIVEN</li>
    <li>3. CMYK &amp; RGB COLOR MODE</li>
    <li>4. 300 DPI JOG, TIFF, PNG, BMP FILES</li>
  </ol>
</main>
</body>
</html>
```